Kestrel Ridge Plumbing Business card & letter head design

We need a new business card and letter head for our plumbing company called kestrel ridge plumbing. attached is the companys logo. We provide domestic and commercial plumbing services in regional western Australia. We are after Something simple yet nice to look at and something that fits within the trade industry.

Target Market(s)

trade/building industry

Contact Information for Business Card

Tarek Holm
Manager
0481 362 714
enquiries@krplumbing.example.au
ABN: 47 153 806 924
PCL: 5318

Domestic & Commercial Plumbing
Tip Truck & Excavator hire

Colors

Designer to choose colors to be used in the design.

```html
<!DOCTYPE html>
<html lang="en">
<head>
<meta charset="utf-8">
<title>Kestrel Ridge Plumbing – Business Card</title>
<link href="https://fonts.googleapis.com/css2?family=Lato:wght@400;700;900&display=swap" rel="stylesheet">
<style>
  :root {
    --backdrop: #4a423d;
    --card: #050708;
    --brand-blue: #1f66c8;
    --text-light: #d9dadb;
    --text-muted: #b4b6b8;
  }
  * { box-sizing: border-box; margin: 0; padding: 0; }
  html, body {
    width: 1200px; height: 847px; overflow: hidden;
    background: var(--backdrop);
    font-family: "Lato", sans-serif;
  }
  .stage { position: relative; width: 1200px; height: 847px; }
  .card {
    position: absolute;
    width: 520px; height: 297px;
    background: var(--card);
    border-radius: 3px;
  }
  .card--front { left: 50px; top: 140px; }
  .card--back { left: 630px; top: 410px; }

  /* front */
  .brand {
    position: absolute; inset: 0;
    display: flex; flex-direction: column; align-items: center; justify-content: center;
    color: var(--brand-blue);
    font-weight: 900;
    text-transform: uppercase;
    line-height: 1.05;
    text-align: center;
  }
  .brand__name { font-size: 40px; letter-spacing: 1px; }
  .brand__trade { font-size: 22px; letter-spacing: 9px; margin-top: 6px; }

  /* back */
  .contact {
    position: absolute; left: 40px; top: 92px;
    width: 215px; text-align: right;
  }
  .contact__name {
    color: var(--brand-blue); font-weight: 700; font-size: 24px;
    text-transform: uppercase; letter-spacing: 0.5px;
  }
  .contact__role { color: var(--text-muted); font-size: 15px; margin-bottom: 10px; }
  .contact__line {
    display: flex; justify-content: flex-end; align-items: center; gap: 8px;
    color: var(--text-light); font-size: 15px; line-height: 1.45;
  }
  .contact__line svg { width: 13px; height: 13px; fill: var(--brand-blue); flex: none; }
  .divider {
    position: absolute; left: 272px; top: 100px;
    width: 1px; height: 100px; background: var(--brand-blue);
  }
  .details {
    position: absolute; left: 290px; top: 112px;
    color: var(--text-light); font-size: 15.5px; line-height: 1.45;
  }
  .details__label { color: var(--brand-blue); }
</style>
</head>
<body>
<main class="stage">
  <section class="card card--front" aria-label="Business card front">
    <div class="brand">
      <span class="brand__name">Kestrel Ridge</span>
      <span class="brand__trade">Plumbing</span>
    </div>
  </section>

  <section class="card card--back" aria-label="Business card back">
    <div class="contact">
      <p class="contact__name">Tarek Holm</p>
      <p class="contact__role">Manager</p>
      <p class="contact__line">0481 362 714
        <svg viewBox="0 0 16 16" aria-hidden="true"><path d="M2 5c0-2 3-3 6-3s6 1 6 3v1h-3V5H5v1H2zM4 7h8l2 6H2zm4 1.5a2 2 0 100 4 2 2 0 000-4z"/></svg>
      </p>
      <p class="contact__line">enquiries@krplumbing.example.au
        <svg viewBox="0 0 16 16" aria-hidden="true"><path d="M1 3h14v10H1zm1.5 1.2v.3L8 8.7l5.5-4.2v-.3zm0 1.9V11.8h11V6.1L8 10.3z"/></svg>
      </p>
    </div>
    <div class="divider"></div>
    <div class="details">
      <p><span class="details__label">ABN:</span> 47 153 806 924</p>
      <p><span class="details__label">PCL:</span> 5318</p>
      <p>Domestic &amp; Commercial Plumbing</p>
      <p>Tip Truck &amp; Excavator hire</p>
    </div>
  </section>
</main>
</body>
</html>
```